Business Card Design

I need a business card for a company based in London, UK. I provide garden design, landscaping and maintenance services. The company specialises in modern, urban gardens. It must be horizontal design, white paper and black simple (easy to read) font. The print must be on clear, white surrounding. I like design that use the colours black, yellow, grey and different shades of green. The design must be tidy. It must not be overloaded with decorating. Embodied a small picture of a fragment of garden or plant or leaf in the sun (it must be yellowish and greenish). It would be good if it's "live and energetic". I attached all text and logo that have to appear on the card.

Target Market(s)

architect, property designers, property management companies, large property owners

Industry/Entity Type

Landscaping

Contact Information for Business Card

All the text must be the same as on my old card which I attached.

Requirements
Must have
• modern, simple, tidy, professional look
green, yellow, black colours,
white surrounding,
simple readable black font on clear white surrounding,
a small picture of garden or plant or "sun lights through the tree canopy"
Nice to have
• graduate movement from light green to dark green
Should not have
• old style font,
text must no be placed on pictures or decorations,
red and blue colours,
picture on the reverse

```html
<!DOCTYPE html>
<html lang="en">
<head>
<meta charset="utf-8">
<title>Bright Leaf Gardens – Business Card</title>
<link rel="stylesheet" href="https://fonts.googleapis.com/css2?family=Questrial&display=swap">
<style>
  :root {
    --backdrop: #e9e9e6;
    --paper: #ffffff;
    --ink: #262626;
    --ink-soft: #4f5553;
    --green-mid: #3fc400;
    --green-light: #7fde22;
    --lime: #b6ec3a;
    --reverse-top: #3ba602;
    --reverse-bottom: #1c5306;
    --photo-leaf: #6f9a5a;
    --photo-haze: #c9d6c4;
    --photo-stone: #b9b39f;
  }
  * { margin: 0; padding: 0; box-sizing: border-box; }
  html, body { width: 1200px; height: 1000px; overflow: hidden; }
  body {
    background: var(--backdrop);
    font-family: "Questrial", "Helvetica Neue", Arial, sans-serif;
    position: relative;
  }
  .card {
    position: absolute;
    left: 325px;
    width: 567px;
    height: 324px;
    box-shadow: 0 4px 10px rgba(0,0,0,0.25);
    overflow: hidden;
  }
  .card--front { top: 141px; background: var(--paper); }
  .card--back {
    top: 517px;
    background: linear-gradient(to bottom, var(--reverse-top), var(--reverse-bottom));
  }
  .garden-photo {
    position: absolute;
    left: 0; top: 0;
    width: 330px; height: 324px;
    background:
      linear-gradient(to right, rgba(255,255,255,0) 35%, #fff 100%),
      linear-gradient(to bottom, var(--photo-haze) 0%, var(--photo-leaf) 45%, var(--photo-stone) 78%, var(--photo-leaf) 100%);
  }
  .brand-name {
    position: absolute;
    right: 20px; top: 68px;
    font-size: 39px;
    font-weight: 400;
    color: var(--ink);
    letter-spacing: 0.4px;
    white-space: nowrap;
  }
  .services {
    position: absolute;
    right: 18px; top: 124px;
    font-size: 25px;
    white-space: nowrap;
  }
  .services .design { color: var(--green-mid); }
  .services .landscaping { color: var(--green-light); }
  .services .maintenance { color: var(--lime); }
  .services .divider { color: var(--green-mid); margin: 0 14px; }
  .contact {
    position: absolute;
    right: 18px; top: 177px;
    text-align: right;
    color: var(--ink-soft);
    font-size: 18px;
    letter-spacing: 0.7px;
    line-height: 22px;
    font-style: normal;
  }
  .contact .web { margin-bottom: 2px; }
  .owner {
    position: absolute;
    right: 18px; top: 279px;
    text-align: right;
    color: var(--ink-soft);
    font-size: 14.5px;
    letter-spacing: 0.6px;
    line-height: 18px;
  }
</style>
</head>
<body>
  <section class="card card--front">
    <div class="garden-photo" role="img" aria-label="Modern urban garden with tree, planting, timber deck and lily pond"></div>
    <h1 class="brand-name">bright leaf gardens</h1>
    <p class="services">
      <span class="design">design</span><span class="divider">|</span><span class="landscaping">landscaping</span><span class="divider">|</span><span class="maintenance">maintenance</span>
    </p>
    <address class="contact">
      <div class="web">www.brightleaf-gardens.co.uk</div>
      <div class="phone">02084417290</div>
      <div class="mobile">07912345618</div>
      <div class="email">info@brightleaf-gardens.co.uk</div>
    </address>
    <div class="owner">
      <div class="owner-name">Adam Kowal</div>
      <div class="owner-address">22 Mill Lane, Richmond, TW9 4QS</div>
    </div>
  </section>
  <section class="card card--back"></section>
</body>
</html>
```